new dating app design - young, fresh, clean

Project Brief

Zivvo is the world's first dating app that actually arranges dates. The process consists of 3 easy steps:

1. use our calendar to tell us when you'd like a date
2. browse singles nearby and select who you'd like to meet
3. when your date is 1 hour away, the app will find you a nice venue in the neighborhood and send one of your matches there to meet you. All you need to do is show up and have a good time.

This design assignment consists of creating a fun, fresh & user-friendly design for the wireframes created by our UX designer. Included are 2 screens:

1. the 'calendar' screen

2. the 'matches' screen

Also included is our style guide for your reference. Feel free to use as much or as little from this guide as you please. It would be nice if we could remain somewhat consistent with our previous design (which was purely based on this style guide) but we also want you to be creative and show off your skills so by no means should you feel obliged to conform to it.

Things to consider

1. 'calendar'

this is where you tell the app when you're free for a date. You can select as many time slots as you want. The info bars at the top and the bottom are 'sticky' (will stay in place no matter where in the screen you scroll to).

Everything about this page needs to be designed: not just in terms of spacing, font and coloring of the calendar itself but also the sticky bars at the bottom and top, and the interactions (when you select a time slot, what happens visually? How will it show that this slot was selected?).

TIP: please ignore the black vs white time slot distribution you see in the image. This was meant to signify where daytime becomes nighttime and vice versa, but we're not doing that anymore. So the only difference between blocks will be the difference between a selected and an unselected block. Make sure that difference is clearly visible in your design.

2. 'matches'

this is where you tell the app whom you'd like to meet with. You can select as many people as you want by clicking their 'heart' icon. You can scroll down to see more people and again the info bars at the top and/or bottom are sticky. The design elements for this page are:

a. the page itself (sizing, spacing of the images, etc.)
b. the interactions (how does a selected heart look, how does that compare to an unselected heart)

ICONS: feel free to come up with your own iconography (ie for the 'chat' icon in the top right, and/or the 'heart' icon signifying you want to meet this person. We really like the fact that the 'matches' and 'calendar' tabs are signified with words rather than icons, but feel free to get creative on this front as well. If you can make it prettier, we're all ears :) Whatever you do on this front, make sure all your icons and the rest of your work are/is free of copyright so we can actually use them in a commercially distributed app.

The winner of this contest may get awarded a follow-up project where they will be asked to design the entire app for us.

Reason: Thank you all for your submissions. We got some promising designs but nothing that was good enough just yet. We gave some feedback for improvement and wanted to give you guys some more time to get it right. New submissions are welcome too of course. Don't hesitate to contact us if you have any questions.

Target Market(s)

singles

Industry/Entity Type

Dating

Requirements
Must have
• fresh, clean, user-friendly design of the 2 pages provided. Your design choices should include decisions about font, sizing, colours, spacing, etc.
Nice to have
• custom icons, see project brief

```html
<!DOCTYPE html>
<html lang="en">
<head>
<meta charset="utf-8">
<title>Zivvo Home – Matches</title>
<link rel="stylesheet" href="https://fonts.googleapis.com/css2?family=Roboto:wght@400;500&display=swap">
<style>
:root{
  --orange:#f8a95a;
  --coral:#f7817b;
  --tab-dim:#fbc7a6;
  --white:#ffffff;
  --card-label:#ececec;
  --name:#5a5a5a;
  --heart-on:#f46b6d;
  --heart-off:#c9c9c9;
  --tip:#73c7e6;
  --fab:#f47a78;
  --banner-green:#6ccaa0;
  --banner-blue:#7ccbe4;
  --banner-ink:#3b4a6b;
  --page:#ffffff;
}
*{box-sizing:border-box;margin:0;padding:0}
html,body{width:675px;height:1200px;overflow:hidden;background:var(--page)}
body{font-family:"Roboto",sans-serif;position:relative}
.header{position:absolute;left:0;top:0;width:675px;height:210px;background:linear-gradient(100deg,var(--orange),var(--coral));color:var(--white)}
.status{position:absolute;top:0;left:0;right:0;height:40px;font-size:15px}
.status .time{position:absolute;left:0;right:0;top:10px;text-align:center}
.status .battery{position:absolute;right:10px;top:10px}
.status .signal{position:absolute;left:10px;top:11px}
.title{position:absolute;left:0;right:0;top:70px;text-align:center;font-size:26px;font-weight:400;letter-spacing:.5px}
.menu{position:absolute;left:24px;top:74px}
.pin{position:absolute;left:609px;top:65px;width:42px;height:42px;border-radius:50%;background:var(--white);display:flex;align-items:center;justify-content:center}
.tabs{position:absolute;top:155px;left:0;width:675px;display:flex;font-size:22px}
.tab{width:50%;text-align:center}
.tab.dim{color:var(--tab-dim)}
.underline{position:absolute;left:0;top:207px;width:338px;height:3px;background:var(--white)}
.card{position:absolute;width:303px;height:226px;background:var(--card-label);box-shadow:0 2px 4px rgba(0,0,0,.18)}
.photo{height:225px;width:100%}
.label{height:57px;display:flex;align-items:center;justify-content:space-between;padding:0 18px 0 24px;font-size:25px;color:var(--name)}
.label b{font-weight:500}
.card.tall{height:282px}
.tip{position:absolute;left:341px;top:229px;width:310px;height:55px;background:var(--tip);color:var(--white);font-size:19px;display:flex;align-items:center;justify-content:center;box-shadow:0 2px 4px rgba(0,0,0,.15)}
.tip::before{content:"";position:absolute;top:-11px;left:154px;border:11px solid transparent;border-top:0;border-bottom-color:var(--tip)}
.fab{position:absolute;left:559px;top:996px;width:92px;height:92px;border-radius:50%;background:var(--fab);display:flex;align-items:center;justify-content:center;box-shadow:0 3px 6px rgba(0,0,0,.2)}
.banner{position:absolute;left:0;top:1104px;width:675px;height:96px;background:linear-gradient(90deg,var(--banner-green),var(--banner-blue));color:var(--white);font-size:20px;text-align:center;line-height:33px;padding-top:16px}
.banner em{font-style:normal;color:var(--banner-ink)}
.banner svg{vertical-align:-3px;margin:0 8px}
</style>
</head>
<body>
<header class="header">
  <div class="status">
    <span class="signal">●●●●● </span>
    <span class="time">9:41 PM</span>
    <span class="battery">100% ▭</span>
  </div>
  <svg class="menu" width="32" height="24" viewBox="0 0 32 24"><g fill="#fff"><rect y="0" width="32" height="3"/><rect y="10.5" width="32" height="3"/><rect y="21" width="32" height="3"/></g></svg>
  <h1 class="title">ZIVVO HOME</h1>
  <div class="pin"><svg width="18" height="24" viewBox="0 0 18 24"><path d="M9 1.5a7 7 0 0 1 7 7c0 5-7 13.5-7 13.5S2 13.5 2 8.5a7 7 0 0 1 7-7z" fill="none" stroke="#333" stroke-width="2"/><text x="9" y="12" font-size="9" text-anchor="middle" fill="#333" font-family="Roboto,sans-serif">?</text></svg></div>
  <nav class="tabs"><span class="tab">MATCHES</span><span class="tab dim">SCHEDULE</span></nav>
  <div class="underline"></div>
</header>

<div class="card" style="left:24px;top:238px"><div class="photo" role="img" aria-label="Profile photo of Angela" style="background:linear-gradient(160deg,#a89a7e,#c9a089 55%,#6b4a34)"></div><div class="label"><span><b>Angela,</b> 21</span><svg width="28" height="25" viewBox="0 0 28 25"><path d="M14 24 2.5 13A7 7 0 0 1 14 4a7 7 0 0 1 11.5 9z" fill="var(--heart-on)"/></svg></div></div>
<div class="card" style="left:348px;top:238px"><div class="photo" role="img" aria-label="Profile photo of Dayna" style="background:linear-gradient(160deg,#7a5e4c,#d7a78e 50%,#8a6a58)"></div><div class="label"><span><b>Dayna,</b> 23</span><svg width="28" height="25" viewBox="0 0 28 25"><path d="M14 24 2.5 13A7 7 0 0 1 14 4a7 7 0 0 1 11.5 9z" fill="var(--heart-off)"/></svg></div></div>
<div class="card" style="left:24px;top:543px"><div class="photo" role="img" aria-label="Profile photo of Oliver" style="background:linear-gradient(160deg,#5d8a4a,#e6c2ae 50%,#7a3c2c)"></div><div class="label"><span><b>Oliver,</b> 18</span><svg width="28" height="25" viewBox="0 0 28 25"><path d="M14 24 2.5 13A7 7 0 0 1 14 4a7 7 0 0 1 11.5 9z" fill="var(--heart-off)"/></svg></div></div>
<div class="card" style="left:348px;top:543px"><div class="photo" role="img" aria-label="Profile photo of Lee" style="background:linear-gradient(160deg,#3a2a22,#e4c0b0 50%,#b04a3a)"></div><div class="label"><span><b>Lee,</b> 25</span><svg width="28" height="25" viewBox="0 0 28 25"><path d="M14 24 2.5 13A7 7 0 0 1 14 4a7 7 0 0 1 11.5 9z" fill="var(--heart-on)"/></svg></div></div>
<div class="card" style="left:24px;top:847px"><div class="photo" role="img" aria-label="Profile photo of Lunsu" style="background:linear-gradient(160deg,#4a3630,#e8cfc4 50%,#5a7eb8)"></div><div class="label"><span><b>Lunsu,</b> 23</span><svg width="28" height="25" viewBox="0 0 28 25"><path d="M14 24 2.5 13A7 7 0 0 1 14 4a7 7 0 0 1 11.5 9z" fill="var(--heart-off)"/></svg></div></div>
<div class="card" style="left:348px;top:847px"><div class="photo" role="img" aria-label="Profile photo of Anay" style="background:linear-gradient(160deg,#7f9a6a,#e2c0a2 50%,#9aa77a)"></div><div class="label"><span><b>Anay,</b> 27</span><svg width="28" height="25" viewBox="0 0 28 25"><path d="M14 24 2.5 13A7 7 0 0 1 14 4a7 7 0 0 1 11.5 9z" fill="var(--heart-off)"/></svg></div></div>

<div class="tip">SET YOUR SCHEDULE HERE</div>

<div class="fab"><svg width="42" height="36" viewBox="0 0 42 36"><path d="M21 3c10 0 18 6 18 13.5S31 30 21 30c-2 0-4-.3-5.8-.8L8 33l1.8-6.5C5.6 24 3 20.5 3 16.5 3 9 11 3 21 3z" fill="none" stroke="#222" stroke-width="2.5"/><g fill="#5fc9a8"><circle cx="14" cy="16.5" r="2"/><circle cx="21" cy="16.5" r="2"/><circle cx="28" cy="16.5" r="2"/></g></svg></div>

<footer class="banner">
  <div><em>EXCELLENT!</em> YOU CAN<svg width="26" height="23" viewBox="0 0 28 25"><path d="M14 24 2.5 13A7 7 0 0 1 14 4a7 7 0 0 1 11.5 9z" fill="#fff"/></svg>MORE IF YOU'D LIKE, NEXT,</div>
  <div>SHARE YOUR SCHEDULE WITH US!</div>
</footer>
</body>
</html>
```